A landing page for an exclusive club VELKARDO

We need a fresh, stylish and luxury design for a landing page of an international private club called VELKARDO.

After receiving your first drafts, let me briefly emphasize some important points:
1) Top picture: I would like to see here some good looking intelligent people (not dancing teenagers or smiling couple – because it’s not a pure dating website)
2) Member’s section: the main message of this slide is to communicate the idea of EXCLUSIVITY - the club has exclusive audience (well-educated, intellectual, financially successful people from world-leading universities and well-known companies). I do not want to reveal real members’ profiles on this slide (it’s allowed only in the review section)
3) Event section should not have real future events, just describe event categories.
4) Technology section should communicate the idea of sending REAL presents (a drink or flowers) to a girl via the app. (maybe by using some dynamic elements during the scrolling)
5) Review section – please make it individual design, not a standard one. Please add company’s names and job titles to reviewers.
6) Event section: we will not post actual events, rather some event categories with large attractive pictures.
7) Technical note: We do not have “register” button – people can log in or register only via QN – it’s one button
Let me know if you have any questions. Thank you for participating!

Kind regards,
Teodor Vashkin

Reason: Dear designers, I have to extend the deadline as I did not receive any 5* designs so far. I would like to get a unique design - not a combination of standard blocks for landing pages. I understand the task is difficult, so I decided to give you more time to prepare well-though and original piece of art. Please use the text from the brief and add your ideas. The 3 main messages to communicate are: 1) Member’s section: the main message of this slide is to communicate the idea of EXCLUSIVITY - the club has exclusive audience (well-educated, intellectual, successful people from world-leading universities and well-known companies). I do not want to reveal real members’ profiles on this slide (it’s allowed only in the review section). 2) Event section: the club runs lots of invitation-only events in most exclusive venues. We will not post actual events, but rather some event categories with large attractive pictures and short descriptions. 3) Technology section should communicate the idea of sending REAL presents (a drink or flowers) to a girl via the app. If you can show it by using some dynamic elements during the scrolling it's fantastic! Good luck! I look forward for your creative ideas and art! Kind regards, Teodor Vashkin

Target Market(s)

Alumni of top universities, middle- and top-level managers of large companies, financial professionals (investment bankers), successful entrepreneurs, recognized creative class (fashion designers, models).

Industry/Entity Type

Club

Coding

Coded - Design and coding required

Number of Pages Required

2 page

Font styles to use
Serif
Sans Serif
Other font styles liked:
• Lato, Oswald, Raleway

Requirements
Must have
• Adaptive design (desktop & mobile)
• Elegant and luxury design
• Structure according to the brief
Nice to have
• Dynamic elements/Layers on the landing page
Should not have
• Trivial stock photos.

```html
<!DOCTYPE html>
<html lang="en">
<head>
<meta charset="utf-8">
<title>VELKARDO – International Private Club</title>
<link href="https://fonts.googleapis.com/css2?family=Raleway:wght@300;400;500;600;700&family=Lato:wght@300;400;700&display=swap" rel="stylesheet">
<style>
:root{
  --blue:#1f7cc1;
  --blue-deep:#1b6fb0;
  --ink:#1d1d1d;
  --text:#333;
  --panel:#efefef;
  --dark:#2f2f2f;
  --footer-bar:#2b2b2b;
  --white:#fff;
  --line:#cfcfcf;
}
*{box-sizing:border-box;margin:0;padding:0}
html,body{width:1200px;height:2799px;overflow:hidden;background:var(--white)}
body{position:relative;font-family:"Lato",Arial,sans-serif;color:var(--text)}
h2,h3,h4{font-weight:400}
.abs{position:absolute}

/* hero */
.hero{left:0;top:0;width:1200px;height:595px;
  background:
    radial-gradient(ellipse 220px 260px at 790px 210px,rgba(236,200,170,.85),rgba(236,200,170,0) 70%),
    radial-gradient(ellipse 300px 200px at 840px 520px,rgba(240,236,240,.9),rgba(240,236,240,0) 70%),
    radial-gradient(ellipse 180px 240px at 330px 230px,rgba(222,190,150,.85),rgba(222,190,150,0) 70%),
    radial-gradient(ellipse 260px 180px at 250px 500px,rgba(170,190,215,.8),rgba(170,190,215,0) 70%),
    radial-gradient(ellipse 160px 300px at 130px 200px,rgba(200,110,70,.7),rgba(200,110,70,0) 70%),
    radial-gradient(ellipse 200px 300px at 1100px 180px,rgba(120,90,70,.8),rgba(120,90,70,0) 70%),
    linear-gradient(100deg,#6e4a36 0%,#a9785a 25%,#8b6c58 50%,#5d4a40 75%,#3b302a 100%)}
.brand{left:78px;top:22px;width:280px;text-align:center;color:var(--white)}
.brand-mark{width:64px;height:64px;border:3px solid var(--white);border-radius:50%;margin:0 auto 16px}
.brand-name{font-family:"Raleway",sans-serif;font-weight:400;font-size:22px;letter-spacing:13px;padding-left:13px}
.menu{left:1082px;top:40px;width:36px}
.menu span{display:block;height:2px;background:var(--white);margin-bottom:7px}
.play{left:562px;top:260px;width:74px;height:74px;border:3px solid var(--white);border-radius:50%;background:rgba(0,0,0,.3)}
.hero-cta{left:285px;top:474px;font-family:"Raleway",sans-serif;font-weight:700;font-size:22px;color:var(--white);text-shadow:0 1px 3px rgba(0,0,0,.5)}
.login-btn{left:620px;top:461px;width:294px;height:56px;background:#3d5e9e;border:3px solid #5b7cc0;display:flex;align-items:center;gap:14px;padding-left:14px;color:var(--white);font-family:"Raleway",sans-serif;font-weight:600;font-size:21px}
.login-btn i{width:34px;height:34px;background:var(--white);display:block}

/* intro */
.intro{left:0;top:614px;width:1200px;text-align:center;font-family:"Raleway",sans-serif;font-weight:600;font-size:19px;line-height:34px;color:var(--ink)}

/* members */
.members-panel{left:0;top:700px;width:606px;height:401px;background:var(--panel)}
.members-photo{left:606px;top:700px;width:594px;height:401px;
  background:
    radial-gradient(ellipse 90px 170px at 110px 270px,rgba(232,190,150,.9),rgba(232,190,150,0) 70%),
    radial-gradient(ellipse 110px 190px at 250px 270px,rgba(236,222,160,.95),rgba(236,222,160,0) 70%),
    radial-gradient(ellipse 110px 190px at 390px 280px,rgba(225,230,236,.95),rgba(225,230,236,0) 70%),
    radial-gradient(ellipse 80px 170px at 540px 290px,rgba(110,40,50,.85),rgba(110,40,50,0) 70%),
    radial-gradient(ellipse 220px 60px at 420px 40px,rgba(245,240,230,.95),rgba(245,240,230,0) 70%),
    linear-gradient(180deg,#5d7446 0%,#7f8a62 30%,#4a4a3c 65%,#2e2c28 100%)}
.section-shadow{left:0;top:1101px;width:1200px;height:14px;background:linear-gradient(rgba(0,0,0,.12),rgba(0,0,0,0))}
.members-title{left:80px;top:752px;font-family:"Raleway",sans-serif;font-weight:400;font-size:30px;color:var(--ink)}
.members-dot{left:80px;top:803px;width:8px;height:8px;border-radius:50%;background:#777}
.members-text{left:80px;top:825px;width:440px;font-size:15px;line-height:28px;color:var(--text)}
.btn-dark{left:80px;top:988px;width:201px;height:50px;background:var(--dark);color:var(--white);font-family:"Lato",sans-serif;font-weight:700;font-size:14px;display:flex;align-items:center;justify-content:center}

/* headings */
.sec-title{left:0;width:1200px;text-align:center;font-family:"Raleway",sans-serif;font-weight:300;font-size:30px;color:var(--ink)}
.sec-title b{color:var(--blue);font-weight:600}
.divider{left:349px;width:502px;height:1px;background:var(--line)}
.divider::after{content:"";position:absolute;left:247px;top:-4px;width:9px;height:9px;border-radius:50%;background:var(--blue)}

/* events */
.events-lead{left:210px;top:1214px;width:780px;text-align:center;font-size:14px;line-height:25px;color:var(--text)}
.event{top:1296px;width:240px;text-align:center}
.event-img{width:200px;height:200px;border-radius:50%;margin:0 auto 22px}
.event h3{font-family:"Raleway",sans-serif;font-weight:700;font-size:16px;color:var(--ink);margin-bottom:8px}
.event p{font-size:13px;line-height:19px;color:var(--text)}
.arrow{width:40px;height:96px}

/* app */
.app-band{left:0;top:1618px;width:1200px;height:453px;background:linear-gradient(135deg,#2c7fc4 0%,#3e93d4 50%,#2a7bbf 100%)}
.app-title{left:90px;top:1656px;width:660px;font-family:"Raleway",sans-serif;font-weight:700;font-size:16px;line-height:29px;color:var(--white)}
.feature-icon{left:88px;width:58px;height:58px;border-radius:50%;background:var(--white)}
.feature-text{left:172px;width:560px;font-size:14px;line-height:25px;color:#eaf3fb}
.download{left:90px;top:1988px;font-family:"Raleway",sans-serif;font-weight:700;font-size:16px;color:var(--white)}
.store{top:1973px;height:52px;background:#111;border:2px solid #888;border-radius:7px;color:var(--white);font-family:"Lato",sans-serif;font-size:19px;display:flex;align-items:center;justify-content:center}
.phone{left:864px;top:1666px;width:252px;height:405px;background:#f4f4f4;border:2px solid #d8d8d8;border-bottom:none;border-radius:36px 36px 0 0}
.phone-screen{left:14px;top:52px;width:220px;height:353px;background:#fff}
.phone-bar{height:28px;background:#222;color:var(--white);font-size:11px;display:flex;align-items:center;justify-content:center}
.phone-grid{display:grid;grid-template-columns:1fr 1fr;grid-auto-rows:118px;gap:3px;padding:3px;height:325px;overflow:hidden}
.tile{border-radius:2px}

/* testimonials */
.quote-box{left:106px;top:2193px;width:989px;height:117px;background:var(--white);box-shadow:0 2px 8px rgba(0,0,0,.18)}
.quote-text{left:180px;top:2211px;width:840px;text-align:center;font-size:13px;line-height:27px;color:var(--text)}
.quote-mark{font-family:Georgia,serif;font-size:54px;color:#9cc3e6;line-height:1}
.avatar{left:109px;top:2333px;width:126px;height:126px;border-radius:50%;background:radial-gradient(circle at 50% 42%,#eccdb4 0%,#c99a78 38%,#7a5a44 62%,#1e1c1b 100%);border:3px solid #eee}
.reviewer{left:261px;top:2374px;font-size:13px;line-height:21px}
.reviewer b{color:var(--blue);font-weight:700;display:block}
.reviewer span{text-decoration:underline;color:var(--ink)}

/* footer */
.footer{left:0;top:2504px;width:1200px;height:248px;background:var(--blue-deep)}
.foot-col{top:2544px;color:var(--white)}
.foot-col h4{font-family:"Raleway",sans-serif;font-weight:600;font-size:22px;padding-bottom:10px;border-bottom:1px solid rgba(255,255,255,.45);margin-bottom:16px}
.foot-col ul{list-style:none;font-size:13px;line-height:28px}
.foot-col li::before{content:"› "}
.foot-divider{top:2540px;width:1px;height:180px;background:rgba(255,255,255,.3)}
.contact-row{display:flex;gap:14px;font-size:13px;line-height:20px;margin-bottom:18px}
.contact-row svg{flex:none}
.email-input{width:258px;height:32px;border:1px solid var(--white);color:#dfeaf5;font-size:12px;font-style:italic;padding:7px 8px;margin:12px 0 10px}
.subscribe{width:112px;height:32px;background:var(--white);color:var(--blue);font-family:"Raleway",sans-serif;font-weight:700;font-size:14px;display:flex;align-items:center;justify-content:center}
.foot-ring{left:974px;top:2549px;width:168px;height:168px;border:4px solid rgba(255,255,255,.35);border-radius:50%}
.bottom-bar{left:0;top:2752px;width:1200px;height:47px;background:var(--footer-bar);color:#bbb;font-size:13px}
.bottom-bar p{position:absolute;left:80px;top:15px}
.bottom-bar b{color:var(--white)}
.social{position:absolute;top:16px;width:14px;height:14px;border-radius:50%;background:#ccc}
.social-sep{position:absolute;top:14px;width:1px;height:18px;background:#555}
</style>
</head>
<body>

<div class="abs hero" role="img" aria-label="Photo of a smiling man and woman talking over coffee at a café table"></div>
<div class="abs brand"><div class="brand-mark"></div><div class="brand-name">VELKARDO</div></div>
<div class="abs menu"><span></span><span></span><span></span></div>
<div class="abs play"><svg width="68" height="68" viewBox="0 0 68 68"><path d="M27 21 L47 34 L27 47 Z" fill="#fff"/></svg></div>
<div class="abs hero-cta">WANT TO JOIN THE CLUB ?</div>
<div class="abs login-btn"><i></i>Login with QN</div>

<p class="abs intro">VELKARDO Club is an international circle of trust which brings together exceptional people<br>committed to building lasting relationships: personal or business .</p>

<div class="abs members-panel"></div>
<div class="abs members-photo" role="img" aria-label="Photo of four smiling club members holding drinks at an outdoor terrace"></div>
<h2 class="abs members-title">Members</h2>
<div class="abs members-dot"></div>
<p class="abs members-text">Club membership is granted based on professional and personal accomplishments, education background, and a social profile of an applicant. Our carefully selected members come from world leading universities, top - tier companies and successful family businesses.</p>
<div class="abs btn-dark">FIND MORE MEMBERS</div>
<div class="abs section-shadow"></div>

<h2 class="abs sec-title" style="top:1138px">PRIVATE <b>EVENTS</b></h2>
<div class="abs divider" style="top:1198px"></div>
<p class="abs events-lead">Every week club members receive invitations for private dinners and parties at the most trendy venues. The club regularly organises weekend trips, private gallery viewings, networking lunches, and various sport activities.</p>

<svg class="abs arrow" style="left:36px;top:1350px" viewBox="0 0 40 96"><path d="M36 2 L4 48 L36 94" fill="none" stroke="#444" stroke-width="2"/></svg>
<svg class="abs arrow" style="left:1124px;top:1350px" viewBox="0 0 40 96"><path d="M4 2 L36 48 L4 94" fill="none" stroke="#444" stroke-width="2"/></svg>

<div class="abs event" style="left:89px"><div class="event-img" role="img" aria-label="Photo of guests celebrating under confetti at a party" style="background:radial-gradient(circle at 35% 30%,#f2f0f6 0%,#9fb6e0 18%,#c2608e 40%,#4b2a6a 70%,#140f24 100%)"></div><h3>Friday parties</h3><p>Lorem ipsum dolor sit amet, consectetur adipiscing elit Sed vitae magna tellus.</p></div>
<div class="abs event" style="left:352px"><div class="event-img" role="img" aria-label="Photo of a long outdoor dinner table with many guests" style="background:radial-gradient(circle at 40% 35%,#f0d08a 0%,#c99a48 30%,#8a4e3a 60%,#33261c 100%)"></div><h3>National meetups</h3><p>Lorem ipsum dolor sit amet, consectetur adipiscing elit Sed vitae magna tellus.</p></div>
<div class="abs event" style="left:611px"><div class="event-img" role="img" aria-label="Photo of people playing a team sport on a court seen from above" style="background:radial-gradient(circle at 50% 45%,#e6ede8 0%,#8fb2a8 35%,#3e7fa0 65%,#2a4a58 100%)"></div><h3>Sport activities</h3><p>Lorem ipsum dolor sit amet, consectetur adipiscing elit Sed vitae magna tellus.</p></div>
<div class="abs event" style="left:871px"><div class="event-img" role="img" aria-label="Photo of a busy banquet hall during a networking lunch" style="background:radial-gradient(circle at 50% 30%,#f4e6c8 0%,#c9a27a 30%,#5e4434 62%,#1c1816 100%)"></div><h3>Networking lunches</h3><p>Lorem ipsum dolor sit amet, consectetur adipiscing elit Sed vitae magna tellus.</p></div>

<div class="abs app-band"></div>
<h2 class="abs app-title">VELKARDO Club Is An International Circle Of Trust Which Brings Together Exceptional People Committed To Building Lasting Relationships: Personal Or Business.</h2>

<div class="abs feature-icon" style="top:1726px"><svg width="58" height="58" viewBox="0 0 58 58"><rect x="20" y="16" width="18" height="24" rx="2" fill="var(--blue)"/><path d="M24 24h10M24 29h10M24 34h7" stroke="#fff" stroke-width="2"/></svg></div>
<p class="abs feature-text" style="top:1722px">Candidates apply for membership on VELKARDO's website and mobile app. All applications are reviewed by our international committee of trustees.</p>
<div class="abs feature-icon" style="top:1810px"><svg width="58" height="58" viewBox="0 0 58 58"><circle cx="29" cy="23" r="7" fill="var(--blue)"/><path d="M17 41c0-8 5-12 12-12s12 4 12 12z" fill="var(--blue)"/></svg></div>
<p class="abs feature-text" style="top:1794px">To join the Club applicants need to satisfy the Club's requirements: our carefully selected members come from the world's leading universities, top-tier companies, governments and successful family businesses.</p>
<div class="abs feature-icon" style="top:1894px"><svg width="58" height="58" viewBox="0 0 58 58"><rect x="17" y="19" width="24" height="21" rx="2" fill="none" stroke="var(--blue)" stroke-width="3"/><path d="M17 25h24M23 15v6M35 15v6" stroke="var(--blue)" stroke-width="3"/><circle cx="29" cy="32" r="3" fill="var(--blue)"/></svg></div>
<p class="abs feature-text" style="top:1878px">Club members participate in regular private events and weekend trips, discover, meet and socialise with similar high - calibre people and receive exclusive privileges from inspirational brands.</p>

<div class="abs download">Download App:</div>
<div class="abs store" style="left:233px;width:159px">Playdeck</div>
<div class="abs store" style="left:418px;width:147px">Appvault</div>

<div class="abs phone">
  <div class="abs phone-screen">
    <div class="phone-bar">Club members</div>
    <div class="phone-grid" role="img" aria-label="Grid of member profile photos in the mobile app">
      <div class="tile" style="background:radial-gradient(circle at 50% 40%,#d9a888,#8a5a44 60%,#5a3a30)"></div>
      <div class="tile" style="background:radial-gradient(circle at 50% 40%,#f0d2b4,#c98a64 55%,#7a3a34)"></div>
      <div class="tile" style="background:radial-gradient(circle at 50% 40%,#e4bc9c,#8a6a58 55%,#3a4a5a)"></div>
      <div class="tile" style="background:radial-gradient(circle at 50% 40%,#c99a7a,#7a5a48 55%,#3e6aa0)"></div>
      <div class="tile" style="background:radial-gradient(circle at 50% 40%,#8a5e48,#4a3028 60%,#d8d8d8)"></div>
      <div class="tile" style="background:radial-gradient(circle at 50% 40%,#e0b898,#9a7a66 55%,#6a6a6a)"></div>
    </div>
  </div>
</div>

<h2 class="abs sec-title" style="top:2106px">Clients <b>Testimonials</b></h2>
<div class="abs divider" style="top:2165px"></div>

<svg class="abs" style="left:40px;top:2236px" width="26" height="58" viewBox="0 0 26 58"><path d="M24 2 L3 29 L24 56" fill="none" stroke="#888" stroke-width="2"/></svg>
<svg class="abs" style="left:1134px;top:2236px" width="26" height="58" viewBox="0 0 26 58"><path d="M2 2 L23 29 L2 56" fill="none" stroke="#888" stroke-width="2"/></svg>

<div class="abs quote-box"></div>
<svg class="abs" style="left:250px;top:2308px" width="36" height="20" viewBox="0 0 36 20"><path d="M0 0 L36 0 L4 20 Z" fill="#fff"/></svg>
<div class="abs quote-mark" style="left:120px;top:2200px">“</div>
<div class="abs quote-mark" style="left:1042px;top:2252px">”</div>
<p class="abs quote-text">Lorem ipsum dolor sitamet, consectetuer adipiscing sed diam nonummy nibh euismod tincidunt ut laoreet dolore magna alqua volutpat. Ut wisi enim ad minim veniam, quis nostrud exerci tation ullamcorper suscipit lobortis nisl ut aliquip ex ea commodo consequat. Duis autem vel eum iriure dolor in hendrerit in vulputate velit esse molestie consequat.</p>

<div class="abs avatar" role="img" aria-label="Portrait photo of the reviewer"></div>
<div class="abs reviewer"><b>Mr. Orlen Pascoe</b><span>Manager, Lorem Ipsum Pvt. Ltd.</span></div>

<div class="abs footer"></div>
<div class="abs foot-col" style="left:80px;width:222px">
  <h4>Quick Links</h4>
  <div style="display:flex;gap:40px">
    <ul><li>Main page</li><li>Privileges</li><li>Contacts</li><li>Partners</li></ul>
    <ul><li>Media</li><li>User agreement</li><li>Confidentiality</li><li>FAQ</li></ul>
  </div>
</div>
<div class="abs foot-divider" style="left:330px"></div>
<div class="abs foot-col" style="left:364px;width:222px">
  <h4>Contact Details</h4>
  <div class="contact-row"><svg width="14" height="20" viewBox="0 0 14 20"><path d="M7 0a7 7 0 0 1 7 7c0 5-7 13-7 13S0 12 0 7a7 7 0 0 1 7-7z" fill="#fff"/><circle cx="7" cy="7" r="2.5" fill="var(--blue-deep)"/></svg><span>Lorem ipsum dolor sit amet,<br>consectetur adipiscing - 12345.</span></div>
  <div class="contact-row"><svg width="14" height="16" viewBox="0 0 14 16"><path d="M3 0l3 4-2 2c1 2 3 4 5 5l2-2 3 3-2 3C6 15-1 8 1 2z" fill="#fff"/></svg><span>012.555.0147</span></div>
  <div class="contact-row" style="margin-top:26px"><svg width="16" height="12" viewBox="0 0 16 12"><rect width="16" height="12" fill="#fff"/><path d="M0 0l8 7 8-7" fill="none" stroke="var(--blue-deep)" stroke-width="1.5"/></svg><span>info@velkardosocialclub.com</span></div>
</div>
<div class="abs foot-divider" style="left:621px"></div>
<div class="abs foot-col" style="left:655px;width:260px">
  <h4>Newsletter Signup</h4>
  <p style="font-size:13px;line-height:19px">Lorem ipsum dolor sit amet conse<br>ctetur adipiscing.</p>
  <div class="email-input">Enter Email Id</div>
  <div class="subscribe">Subscribe</div>
</div>
<div class="abs foot-divider" style="left:942px"></div>
<div class="abs foot-ring"></div>

<div class="abs bottom-bar">
  <p>Copyright © 2016 <b>VELKARDO SOCIAL DISCOVERY CLUB</b>. All Rights Reserved.</p>
  <span class="social" style="left:960px"></span>
  <span class="social-sep" style="left:985px"></span>
  <span class="social" style="left:1003px"></span>
  <span class="social-sep" style="left:1030px"></span>
  <span class="social" style="left:1052px"></span>
  <span class="social-sep" style="left:1080px"></span>
  <span class="social" style="left:1103px"></span>
</div>

</body>
</html>
```